Real Estate Managemene Company Needs Business Card Design

We have a logo design and just need business cards made now for our business. Please use PDF logo # 3.

Card with Information to be attached shortly.

The card is used for a real estate management company. We will need to add four other employees and their cards.

Industry/Entity Type

Real Estate

Contact Information for Business Card

Tariq Nawabi
President
3187 Thornfield Avenue
Suite A
Glendale Heights, IL 60847
Phone 630.471.2286
Fax 630.493.7720
Cell 630.517.8043
pvgrop@mailnest.net

Once design is approved we will have four other employees
Omar Nawabi
Operations Manager

Samira Nawabi
Administrative Manager

Faz Nawabi
Principal

We would need to take out the cell # 630.517.8043 out for the remaining three cards.

Requirements
Must have
• Please use logo attached

```html
<!DOCTYPE html>
<html lang="en">
<head>
<meta charset="utf-8">
<title>Harborline Property Management Group – Business Card</title>
<link href="https://fonts.googleapis.com/css2?family=Open+Sans:wght@400;600&display=swap" rel="stylesheet">
<style>
  :root {
    --page: #e9e7e3;
    --card: #ffffff;
    --brand-blue: #0f5a8e;
    --ink: #1b1b1b;
    --dark-bar: #222222;
    --white: #ffffff;
  }
  * { margin: 0; padding: 0; box-sizing: border-box; }
  html, body { width: 1200px; height: 1000px; overflow: hidden; }
  body {
    background: var(--page);
    font-family: "Open Sans", Arial, sans-serif;
    color: var(--ink);
    position: relative;
  }
  .card {
    position: absolute;
    left: 265px;
    width: 666px;
    height: 397px;
    overflow: hidden;
    box-shadow: 0 3px 8px rgba(0,0,0,0.18);
  }
  .card--front { top: 73px; background: var(--card); }
  .card--back { top: 532px; background: var(--brand-blue); }

  .brand {
    position: absolute;
    left: 0; right: 0;
    display: flex;
    flex-direction: column;
    align-items: center;
    text-align: center;
  }
  .card--front .brand { top: 92px; }
  .card--back .brand { top: 98px; }
  .brand__mark {
    width: 34px; height: 34px;
    background: var(--brand-blue);
    margin-bottom: 18px;
  }
  .card--back .brand__mark { background: var(--white); }
  .brand__name {
    font-weight: 600;
    font-size: 30px;
    letter-spacing: 2px;
    line-height: 1.15;
    text-transform: uppercase;
    color: var(--ink);
  }
  .card--back .brand__name { color: var(--white); }

  .contact {
    position: absolute;
    top: 268px;
    left: 0; right: 0;
    font-size: 15px;
    line-height: 1;
  }
  .contact__person {
    position: absolute;
    right: 353px;
    top: 0;
    text-align: right;
  }
  .contact__name {
    color: var(--brand-blue);
    font-size: 18px;
    letter-spacing: 0.5px;
    text-transform: uppercase;
    margin-bottom: 8px;
  }
  .contact__title { margin-bottom: 15px; }
  .contact__address span { display: block; margin-bottom: 6px; }
  .contact__divider {
    position: absolute;
    left: 332px;
    top: 4px;
    width: 1px;
    height: 90px;
    background: var(--ink);
  }
  .contact__lines {
    position: absolute;
    left: 351px;
    top: 2px;
    list-style: none;
  }
  .contact__lines li {
    display: flex;
    align-items: center;
    height: 25px;
  }
  .contact__lines svg {
    width: 14px; height: 14px;
    margin-right: 11px;
    fill: var(--brand-blue);
  }

  .footer-bar {
    position: absolute;
    bottom: 0;
    height: 10px;
  }
  .footer-bar--blue { left: 0; width: 330px; background: var(--brand-blue); }
  .footer-bar--dark { left: 335px; right: 0; background: var(--dark-bar); }
</style>
</head>
<body>

<section class="card card--front">
  <div class="brand">
    <div class="brand__mark"></div>
    <div class="brand__name">Harborline<br>Property Management Group</div>
  </div>

  <div class="contact">
    <div class="contact__person">
      <p class="contact__name">Tariq Nawabi</p>
      <p class="contact__title">President</p>
      <p class="contact__address">
        <span>3187 Thornfield Avenue, Suite A</span>
        <span>Glendale Heights, IL 60847</span>
      </p>
    </div>
    <div class="contact__divider"></div>
    <ul class="contact__lines">
      <li>
        <svg viewBox="0 0 14 14" aria-hidden="true"><path d="M4 0h1v2h4a1 1 0 0 1 1 1v10a1 1 0 0 1-1 1H5a1 1 0 0 1-1-1zM5 3v4h4V3z"/></svg>
        630.517.8043
      </li>
      <li>
        <svg viewBox="0 0 14 14" aria-hidden="true"><path d="M0 5c2-3 12-3 14 0l-1 2-3-1V4H4v2L1 7zM3 8h8l2 5H1z"/></svg>
        630.471.2286
      </li>
      <li>
        <svg viewBox="0 0 14 14" aria-hidden="true"><path d="M3 1h8v3H3zM0 5h14v6h-3V9H3v2H0zM4 10h6v4H4z"/></svg>
        630.493.7720
      </li>
      <li>
        <svg viewBox="0 0 14 14" aria-hidden="true"><path d="M0 3h14v1L7 8 0 4zM0 5.5l7 4 7-4V11H0z"/></svg>
        www.pvgrop@mailnest.net
      </li>
    </ul>
  </div>

  <div class="footer-bar footer-bar--blue"></div>
  <div class="footer-bar footer-bar--dark"></div>
</section>

<section class="card card--back">
  <div class="brand">
    <div class="brand__mark"></div>
    <div class="brand__name">Harborline<br>Property Management Group</div>
  </div>
</section>

</body>
</html>
```